Morvela Aesthetic Doctor

I require an elegant, luxurious looking business card for my aesthetic business. I am a doctor and that will set me aside from competitors. I am planning to provide home and spa based treatments to clients with high expectations. I have attached my logo.

```html
<!DOCTYPE html>
<html lang="en">
<head>
<meta charset="utf-8">
<title>Morvela Aesthetic Doctor – Business Card</title>
<link rel="stylesheet" href="https://fonts.googleapis.com/css2?family=Lato:wght@400;700&display=swap">
<style>
  :root {
    --page-bg: #e9e9e9;
    --card-bg: #333333;
    --accent: #7ecbea;
    --accent-strong: #6fc3ec;
    --text-light: #f2f2f2;
    --band-text: #333333;
  }
  * { box-sizing: border-box; margin: 0; padding: 0; }
  html, body {
    width: 1200px; height: 1200px; overflow: hidden;
    background: var(--page-bg);
    font-family: "Lato", sans-serif;
  }
  .card {
    position: absolute;
    left: 188px;
    width: 830px;
    height: 478px;
    background: var(--card-bg);
    color: var(--text-light);
  }
  .card--front { top: 83px; }
  .card--back { top: 647px; }

  .brand {
    position: absolute;
    left: 36px;
    top: 190px;
    display: flex;
    align-items: center;
    gap: 16px;
  }
  .brand__mark {
    width: 92px; height: 92px;
    border: 2px solid var(--text-light);
    border-radius: 50%;
    flex: none;
  }
  .brand__name {
    font-weight: 400;
    color: var(--text-light);
    line-height: 1;
  }
  .brand__name-main {
    display: block;
    font-size: 44px;
    letter-spacing: 3px;
  }
  .brand__name-sub {
    display: block;
    font-size: 19px;
    letter-spacing: 2.2px;
    margin-top: 8px;
  }

  .divider {
    position: absolute;
    left: 414px;
    top: 165px;
    width: 2px;
    height: 150px;
    background: var(--accent);
  }

  .details {
    position: absolute;
    left: 454px;
    top: 164px;
  }
  .details__name {
    font-size: 22px;
    font-weight: 400;
    white-space: nowrap;
  }
  .details__name-person { color: var(--accent-strong); font-weight: 700; }
  .details__diploma {
    font-size: 17px;
    margin-top: 6px;
    white-space: nowrap;
  }
  .contact {
    list-style: none;
    margin-top: 18px;
  }
  .contact__item {
    display: flex;
    align-items: center;
    gap: 10px;
    font-size: 20px;
    height: 29px;
  }
  .contact__icon { width: 18px; height: 18px; flex: none; }
  .contact__social {
    display: inline-block;
    width: 16px; height: 16px;
    border-radius: 50%;
    background: var(--accent);
    margin-left: 4px;
  }

  .services {
    position: absolute;
    left: 452px;
    top: 152px;
    list-style: none;
  }
  .services__item {
    display: flex;
    align-items: center;
    font-size: 21px;
    height: 28.3px;
    white-space: nowrap;
  }
  .services__item::before {
    content: "";
    width: 8px; height: 8px;
    border-radius: 50%;
    background: var(--accent);
    margin-right: 11px;
  }

  .tagline {
    position: absolute;
    left: 0; bottom: 0;
    width: 100%;
    height: 44px;
    background: var(--accent);
    color: var(--band-text);
    font-size: 18px;
    display: flex;
    align-items: center;
    justify-content: center;
    letter-spacing: 0.1px;
  }
</style>
</head>
<body>

<section class="card card--front">
  <div class="brand">
    <span class="brand__mark"></span>
    <div class="brand__name">
      <span class="brand__name-main">MORVELA</span>
      <span class="brand__name-sub">AESTHETIC DOCTOR</span>
    </div>
  </div>
  <span class="divider"></span>
  <div class="details">
    <p class="details__name"><span class="details__name-person">Dr Elise Varenne,</span> MRCPCH MD</p>
    <p class="details__diploma">Australasian Diploma of Aesthetic Medicine</p>
    <ul class="contact">
      <li class="contact__item">
        <svg class="contact__icon" viewBox="0 0 24 24" fill="none" stroke="#7ecbea" stroke-width="2" stroke-linecap="round" stroke-linejoin="round"><path d="M22 16.9v3a2 2 0 0 1-2.2 2 19.8 19.8 0 0 1-8.6-3.1 19.5 19.5 0 0 1-6-6A19.8 19.8 0 0 1 2.1 4.2 2 2 0 0 1 4.1 2h3a2 2 0 0 1 2 1.7c.1 1 .4 1.9.7 2.8a2 2 0 0 1-.5 2.1L8 9.8a16 16 0 0 0 6 6l1.3-1.3a2 2 0 0 1 2.1-.4c.9.3 1.8.6 2.8.7a2 2 0 0 1 1.7 2z"/><path d="M15 5a5 5 0 0 1 4 4M15 1a9 9 0 0 1 8 8"/></svg>
        <span>0800 555 014</span>
      </li>
      <li class="contact__item">
        <svg class="contact__icon" viewBox="0 0 24 24" fill="#7ecbea"><path d="M2 6h20v12H2z"/><path d="M2 6l10 7 10-7M2 18l7-6M22 18l-7-6" fill="none" stroke="#333" stroke-width="1.6"/></svg>
        <span>elise@morvela.co.nz</span>
      </li>
      <li class="contact__item">
        <svg class="contact__icon" viewBox="0 0 24 24" fill="none" stroke="#7ecbea" stroke-width="1.6"><circle cx="12" cy="12" r="10"/><ellipse cx="12" cy="12" rx="4.5" ry="10"/><path d="M2 12h20M4 6.5h16M4 17.5h16"/></svg>
        <span>www.morvela.co.nz</span>
        <span class="contact__social"></span>
        <span class="contact__social"></span>
      </li>
    </ul>
  </div>
  <div class="tagline">HOME AND SPA BASED TREATMENTS</div>
</section>

<section class="card card--back">
  <div class="brand">
    <span class="brand__mark"></span>
    <div class="brand__name">
      <span class="brand__name-main">MORVELA</span>
      <span class="brand__name-sub">AESTHETIC DOCTOR</span>
    </div>
  </div>
  <span class="divider"></span>
  <ul class="services">
    <li class="services__item">Dermal injectables</li>
    <li class="services__item">Plasma facials</li>
    <li class="services__item">Microneedling</li>
    <li class="services__item">Skin boosters</li>
    <li class="services__item">Excessive sweating</li>
    <li class="services__item">Home and Spa Based Treatments</li>
  </ul>
  <div class="tagline">HOME AND SPA BASED TREATMENTS</div>
</section>

</body>
</html>
```